Keto Food Brand Needs Packaging Design and Logo

We need a logo and packaging design for a stand-up food bag for our keto shake mix. We are a health and wellness brand launching our first shake mix product. I would like bold, bright colors. This document goes more in depth . This brand might encompass more than only food so I want the logo to be versatile for supplements and other health products. https://files.plimmerdocs.net/sheet/7qXbRt2LmPzK9vWc4HnJ8sFdYa3GeU6oBiN1kT5rQ0Vx/view?mode=shared See images of logos attached. It doesn't have to be food for the logo but I like the creativity of the ones listed.

Target Market(s)

Keto. Health and Fitness

Logo Text

Zunavo

Font styles to use
Serif
Sans Serif

Colors

Designer to choose colors to be used in the design.

```html
<!DOCTYPE html>
<html lang="en">
<head>
<meta charset="utf-8">
<title>Zunavo Keto Cheesecake Shake Mix – Pouch Front</title>
<link href="https://fonts.googleapis.com/css2?family=Outfit:wght@700;800&family=Oswald:wght@500;600;700&display=swap" rel="stylesheet">
<style>
  :root {
    --backdrop: #34beba;
    --pouch-white: #f1f2f3;
    --pouch-shade: #e4e6e8;
    --band-cyan: #43c3da;
    --band-deep: #2fb0cb;
    --ink-charcoal: #2f3336;
    --ink-teal: #0f5a6a;
    --badge-red: #e2262b;
    --paper-white: #ffffff;
    --cake-cream: #efe9cf;
  }
  * { margin: 0; padding: 0; box-sizing: border-box; }
  html, body {
    width: 1126px; height: 1200px; overflow: hidden;
    background: var(--backdrop);
  }
  .pouch {
    position: absolute; left: 271px; top: 212px;
    width: 586px; height: 838px;
    background: linear-gradient(180deg, var(--pouch-white) 0%, var(--pouch-shade) 100%);
    border-radius: 10px;
    overflow: hidden;
    font-family: "Outfit", sans-serif;
  }
  .flavor-band {
    position: absolute; left: 0; right: 0; top: 494px; bottom: 0;
    background: linear-gradient(160deg, var(--band-deep) 0%, var(--band-cyan) 45%, var(--band-cyan) 100%);
  }
  .brand-name {
    position: absolute; left: 0; right: 0; top: 172px;
    text-align: center;
    font-weight: 800; font-size: 42px; line-height: 1; letter-spacing: 1px;
    color: var(--ink-charcoal);
  }
  .keto-word {
    position: absolute; left: 192px;
    font-weight: 800; font-size: 180px; line-height: 1;
    letter-spacing: 4px;
    color: var(--ink-charcoal);
  }
  .keto-top { top: 240px; }
  .keto-bottom { top: 432px; }
  .claims {
    position: absolute; left: 62px; top: 458px; width: 124px;
    list-style: none;
    font-family: "Oswald", sans-serif; font-weight: 600;
    font-size: 14px; line-height: 1.05; color: var(--ink-charcoal);
    text-align: center;
  }
  .claim { padding: 4px 0; }
  .claim + .claim { border-top: 2px solid var(--ink-charcoal); }
  .servings-badge {
    position: absolute; left: 442px; top: 475px;
    width: 76px; height: 76px; border-radius: 50%;
    background: var(--badge-red);
    border: 3px solid var(--paper-white);
    color: var(--paper-white);
    font-family: "Oswald", sans-serif; font-weight: 700;
    text-align: center; transform: rotate(-14deg);
    display: flex; flex-direction: column; justify-content: center;
  }
  .servings-count { font-size: 25px; line-height: 1; }
  .servings-label { font-size: 11px; line-height: 1.1; }
  .product-photo {
    position: absolute; left: 404px; top: 680px;
    width: 150px; height: 82px;
    border-radius: 6px;
    background: linear-gradient(180deg, var(--paper-white) 0%, var(--cake-cream) 100%);
  }
  .flavor-name {
    position: absolute; left: 138px; top: 605px;
    font-family: "Oswald", sans-serif; font-weight: 700;
    font-size: 59px; line-height: 1; letter-spacing: 0.5px;
    color: var(--ink-teal);
  }
  .product-type {
    position: absolute; left: 198px; top: 662px;
    font-family: "Oswald", sans-serif; font-weight: 600;
    font-size: 45px; line-height: 1;
    color: var(--ink-teal);
  }
  .net-weight {
    position: absolute; left: 83px; top: 771px;
    font-family: "Oswald", sans-serif; font-weight: 500;
    font-size: 22px; line-height: 1; color: var(--ink-charcoal);
  }
  .supplement-note {
    position: absolute; left: 379px; top: 772px;
    font-family: "Oswald", sans-serif; font-weight: 500;
    font-size: 16px; line-height: 1; letter-spacing: 0.5px; color: var(--ink-charcoal);
  }
</style>
</head>
<body>
  <main class="pouch">
    <div class="flavor-band"></div>

    <div class="brand-name">ZUNAVO</div>

    <div class="keto-word keto-top">KE</div>
    <div class="keto-word keto-bottom">TO</div>

    <ul class="claims">
      <li class="claim">NO ARTIFICIAL<br>FLAVORS</li>
      <li class="claim">ALL NATURAL</li>
      <li class="claim">KETO-FRIENDLY &amp;<br>LOW CARB</li>
    </ul>

    <div class="servings-badge">
      <span class="servings-count">40</span>
      <span class="servings-label">SERVINGS</span>
    </div>

    <div class="flavor-name">CHEESECAKE</div>
    <div class="product-type">SHAKE MIX</div>

    <div class="product-photo" role="img" aria-label="Slice of cheesecake with a splash of milk"></div>

    <div class="net-weight">Net Wt. 1.02 LB.</div>
    <div class="supplement-note">DIETARY SUPPLEMENT</div>
  </main>
</body>
</html>
```